BRKL informational brochure to aimed to attract people to all three our our service industries

This brochure is designed to be multi purposed, here are a few objectives:
1. To provide a receipt for septic services rendered onsite to customers. The receipt has coupons to entice each customer to use us in the future. This brochure also gives this customer tips on how to best keep their septic system from developing issues. By providing additional company information the septic customer can become educated about the other lines of service we provide in the area, i.e. Trash pick up, & roll-off dumpsters. Optimally we would want a septic customer to be so impressed with our septic work that they would trust us to serve them in the other areas we offer.
2. The brochure is a means of obtaining ratings and reviews for our online profiles, i.e. Zentrix, & Marla's roster. It is already hard enough to get a customer to give us 5-star ratings, so this is a useful tool to try and bait the customer to get a price reduction on their total cost for septic services by rating us or performing an online review. We want to have a place on the brochure that references our current 5-star ratings on Zentrix, Pinwheel, and Marla's roster see the attached example.
3. This brochure is not only useful for septic clients but can also be used for general advertising, we leave these brochures in a variety of public locations. Thus it would be efficient to show all lines of business and provide the information needed to acquire new clients.
4. Photographs are a critical component of our plan, customers like to SEE what we do and who we are. Thus, please find a creative way of including photos of what we offer by means of services and products. For individuals who have seen our brand around town, a photographic reminder might help this potential clients to recognizing who we are.
5. I will attach a copy of our last ArtGather project to this project to give you an idea of how we like to present ourselves.
6. We want to encourage the Spanish speaking individuals to call us for translated material.
7. We need to mention pricing on this brochure for all 3 lines of business, i'll find a way to provide those to you.
8. We don't know what size to choose, one size is 8.5'' x 11'' the other size is 8.5'' x 14'. Perhaps you can help us choose. not sure if we should have a trifold (3 pane) or quadfold (4 pane) brochure. We want to express ourselves creatively and not just provide boring information.
9. we need to have an american flag somewhere on display
Target Market(s)
Rural areas of North Texas, Our office is in Ponder TX and we serve 35 mile radius.
Industry/Entity Type
Waste Management

```html
<!DOCTYPE html>
<html lang="en">
<head>
<meta charset="UTF-8">
<title>BRKL Services Brochure – Inside Spread</title>
<link rel="stylesheet" href="https://fonts.googleapis.com/css2?family=Tinos:ital,wght@0,400;0,700;1,700&display=swap">
<style>
  :root {
    --ink: #111111;
    --charcoal: #1e1f24;
    --charcoal-soft: #2b2c31;
    --red: #e3141b;
    --red-deep: #b80d12;
    --yellow: #f4e51c;
    --gold: #e4b317;
    --paper: #f7f7f5;
    --white: #ffffff;
  }
  * { box-sizing: border-box; margin: 0; padding: 0; }
  html, body { width: 1200px; height: 800px; overflow: hidden; background: #d9d9d9; }
  body { font-family: "Tinos", "Times New Roman", serif; color: var(--ink); }

  .spread { position: relative; width: 1200px; height: 800px; display: flex; }
  .panel { position: relative; width: 400px; height: 800px; overflow: hidden; background: var(--paper); }
  .panel + .panel { border-left: 1px solid rgba(0,0,0,.08); }

  .photo { position: absolute; }
  .photo--field { inset: 0 0 auto 0; height: 540px;
    background: linear-gradient(180deg, #1c1d22 0%, #2a2b2c 45%, #3a3a2c 70%, #24241f 100%); }
  .photo--dark { inset: 0 0 auto 0; height: 540px;
    background: linear-gradient(180deg, #1b1c21 0%, #25262b 60%, #2e2f2a 100%); }
  .photo--dumpsters-roll { left: 40px; top: 330px; width: 320px; height: 170px; border-radius: 4px;
    background: radial-gradient(ellipse at 60% 30%, #5d7390 0%, #1f3048 55%, #16202c 100%); }
  .photo--dumpsters-yard { inset: 0 0 auto 0; height: 330px;
    background: linear-gradient(160deg, #2a2d3a 0%, #3c4154 45%, #d7c21d 70%, #f0d51a 100%); }

  .curve { position: absolute; left: 0; width: 400px; }
  .edge { position: absolute; left: 0; bottom: 0; width: 100%; height: 7px;
    background: linear-gradient(90deg, var(--gold), var(--yellow), var(--gold)); }

  .tick-list { list-style: none; }
  .tick-list li { position: relative; padding-left: 22px; font-weight: 700; }
  .tick-list li svg { position: absolute; left: 0; top: .25em; width: 14px; height: 12px; }

  .hl-yellow { color: var(--yellow); }
  .hl-red { color: var(--red); }
  .rule { width: 44px; height: 3px; background: var(--red); margin: 6px 0 12px; }

  /* panel 1 */
  .deals { position: absolute; left: 42px; top: 60px; color: var(--white); }
  .deals__title { font-size: 21px; font-weight: 700; text-transform: uppercase; color: var(--yellow); }
  .deals .tick-list li { font-size: 17px; line-height: 1.25; }
  .quote { position: absolute; left: 42px; top: 268px; width: 330px; }
  .quote__title { font-size: 30px; font-weight: 700; line-height: 1.05; color: var(--yellow); text-transform: uppercase; letter-spacing: .5px; }
  .phone-pill { display: inline-flex; align-items: center; gap: 10px; margin-top: 14px; padding: 6px 22px;
    background: var(--red); color: var(--white); border: 2px solid var(--yellow); border-radius: 30px;
    font-size: 22px; font-weight: 700; }
  .phone-pill svg { width: 20px; height: 20px; }

  .residential { position: absolute; left: 32px; top: 560px; width: 345px; }
  .section-title { font-size: 20px; font-weight: 700; }
  .lead { font-size: 14px; font-weight: 700; margin-bottom: 4px; }
  .small { font-size: 10.5px; line-height: 1.25; }
  .residential .tick-list { margin: 8px 0 6px; }
  .residential .tick-list li { font-size: 14.5px; line-height: 1.25; }

  /* panel 2 */
  .septic { position: absolute; left: 38px; top: 56px; width: 330px; color: var(--white); }
  .septic__title { font-size: 21px; font-weight: 700; line-height: 1.05; text-transform: uppercase; color: var(--yellow); }
  .septic__title span { color: var(--red); }
  .septic__promise { font-size: 14px; font-weight: 700; text-transform: uppercase; margin-bottom: 6px; }
  .septic p { font-size: 10.5px; line-height: 1.3; margin-bottom: 6px; }
  .septic .price { color: var(--yellow); font-weight: 700; }

  .rolloff { position: absolute; left: 32px; top: 540px; width: 345px; }
  .rolloff .lead { text-transform: uppercase; }
  .haul { font-size: 15px; font-weight: 700; margin-top: 6px; }
  .haul-price { font-size: 18px; font-weight: 700; color: var(--red); }
  .rolloff .tick-list li { font-size: 14.5px; line-height: 1.25; }

  /* panel 3 */
  .other { position: absolute; left: 36px; top: 360px; width: 340px; }
  .other .tick-list li { font-size: 13.5px; line-height: 1.3; }
  .care { position: absolute; left: 36px; top: 500px; width: 340px; }
  .care .tick-list li { font-size: 12.5px; line-height: 1.25; margin-bottom: 3px; }
</style>
</head>
<body>
<main class="spread">

  <!-- Panel: discounts and residential -->
  <section class="panel panel--residential">
    <div class="photo photo--field" role="img" aria-label="Photo of a BRKL service truck parked in a rural field, darkened"></div>
    <svg class="curve" style="top:440px" height="360" viewBox="0 0 400 360" aria-hidden="true">
      <path d="M0,70 Q200,-10 400,40 L400,360 L0,360 Z" fill="var(--red)"/>
      <path d="M0,110 Q200,40 400,62 L400,360 L0,360 Z" fill="var(--paper)"/>
    </svg>

    <div class="deals">
      <h2 class="deals__title">Discounts &amp; <span class="hl-red">Deals</span></h2>
      <div class="rule"></div>
      <ul class="tick-list">
        <li><svg viewBox="0 0 14 12"><path d="M1 6l4 4 8-9" stroke="var(--yellow)" stroke-width="2.4" fill="none"/></svg>Military</li>
        <li><svg viewBox="0 0 14 12"><path d="M1 6l4 4 8-9" stroke="var(--yellow)" stroke-width="2.4" fill="none"/></svg>Senior</li>
        <li><svg viewBox="0 0 14 12"><path d="M1 6l4 4 8-9" stroke="var(--yellow)" stroke-width="2.4" fill="none"/></svg>Seasonal Discounts</li>
        <li><svg viewBox="0 0 14 12"><path d="M1 6l4 4 8-9" stroke="var(--yellow)" stroke-width="2.4" fill="none"/></svg>Clergy</li>
        <li><svg viewBox="0 0 14 12"><path d="M1 6l4 4 8-9" stroke="var(--yellow)" stroke-width="2.4" fill="none"/></svg><span class="hl-yellow">HUGE</span>&nbsp;Referral Bonus</li>
      </ul>
    </div>

    <div class="quote">
      <h2 class="quote__title">Call for<br>a free quote</h2>
      <div class="phone-pill">
        <svg viewBox="0 0 20 20"><circle cx="10" cy="10" r="9" fill="none" stroke="#fff" stroke-width="1.6"/><path d="M7 5.5l1.6 2.4-1 1.2a6 6 0 0 0 3.3 3.3l1.2-1 2.4 1.6-1 1.6c-3.6.2-7.6-3.8-7.4-7.4z" fill="#fff"/></svg>
        940-555-0134
      </div>
    </div>

    <div class="residential">
      <h2 class="section-title">Residential <span class="hl-red">Waste Collections</span></h2>
      <div class="rule"></div>
      <p class="lead">We don’t talk trash, we talk solutions!</p>
      <p class="small">Our local team provides professional, friendly, small-town customer service that you won’t find anywhere else. There are multiple packages to meet any budget:</p>
      <ul class="tick-list">
        <li><svg viewBox="0 0 14 12"><path d="M1 6l4 4 8-9" stroke="var(--red)" stroke-width="2.4" fill="none"/></svg>Toters – <span class="hl-red">starting at $19.99/ per month!</span></li>
        <li><svg viewBox="0 0 14 12"><path d="M1 6l4 4 8-9" stroke="var(--red)" stroke-width="2.4" fill="none"/></svg>2 yard Dumpsters – <span class="hl-red">Start up special $55 per month!</span></li>
        <li><svg viewBox="0 0 14 12"><path d="M1 6l4 4 8-9" stroke="var(--red)" stroke-width="2.4" fill="none"/></svg>Bagged Trash Service</li>
        <li><svg viewBox="0 0 14 12"><path d="M1 6l4 4 8-9" stroke="var(--red)" stroke-width="2.4" fill="none"/></svg>Bulk pick-up &amp; Garage clean outs<br>See all the Discounts above!</li>
      </ul>
      <p class="small">We strive to offer dependable and affordable residential trash removal throughout Denton County &amp; all the surrounding areas.</p>
    </div>
    <div class="edge"></div>
  </section>

  <!-- Panel: septic and roll-off -->
  <section class="panel panel--rolloff">
    <div class="photo photo--dark" role="img" aria-label="Photo of a septic pumping truck at a job site, darkened"></div>
    <div class="photo photo--dumpsters-roll" role="img" aria-label="Photo of blue BRKL roll-off dumpsters lit by sunlight"></div>
    <svg class="curve" style="top:440px" height="360" viewBox="0 0 400 360" aria-hidden="true">
      <path d="M0,62 Q200,60 400,-10 L400,360 L0,360 Z" fill="var(--red)"/>
      <path d="M0,80 Q200,70 400,20 L400,360 L0,360 Z" fill="var(--paper)"/>
    </svg>

    <div class="septic">
      <h2 class="septic__title">Septic Pumping &amp;<br><span>Cleaning</span></h2>
      <div class="rule"></div>
      <p class="septic__promise">Service guaranteed or your waste back!</p>
      <p>Pump &amp; clean services <span class="price">starting at $350 for conventional and $450 for aerobic systems!</span></p>
      <p>We take pride in our work and are dedicated to offering the highest-quality septic pumping services available.</p>
      <p>From cesspools and septic tanks to sewage pits and beyond, you can depend on our experienced technicians to get the job done right. Sit back and relax while we take care of the dirty work.</p>
    </div>

    <div class="rolloff">
      <h2 class="section-title">Roll- <span class="hl-red">Off Dumpsters</span></h2>
      <div class="rule"></div>
      <p class="lead">No project is too big!</p>
      <p class="small">BRKL offer a variety of roll-off and construction dumpsters that are ready to meet the needs of any construction or demolition project. From a small renovation or landscape project, to new building constructions.</p>
      <p class="haul">We provide reliable waste hauling services:</p>
      <p class="haul-price">Staring at $450/ haul</p>
      <ul class="tick-list">
        <li><svg viewBox="0 0 14 12"><path d="M1 6l4 4 8-9" stroke="var(--red)" stroke-width="2.4" fill="none"/></svg>24-hour turn around time</li>
        <li><svg viewBox="0 0 14 12"><path d="M1 6l4 4 8-9" stroke="var(--red)" stroke-width="2.4" fill="none"/></svg>Competitive pricing</li>
        <li><svg viewBox="0 0 14 12"><path d="M1 6l4 4 8-9" stroke="var(--red)" stroke-width="2.4" fill="none"/></svg>Complementary Tonnage</li>
        <li><svg viewBox="0 0 14 12"><path d="M1 6l4 4 8-9" stroke="var(--red)" stroke-width="2.4" fill="none"/></svg>Friendly teammate always available to take your order</li>
      </ul>
    </div>
    <div class="edge"></div>
  </section>

  <!-- Panel: other services and maintenance -->
  <section class="panel panel--septic-care">
    <div class="photo photo--dumpsters-yard" role="img" aria-label="Photo of a dark BRKL dumpster and a yellow front-load bin"></div>
    <svg class="curve" style="top:250px" height="140" viewBox="0 0 400 140" aria-hidden="true">
      <path d="M0,120 Q120,20 400,0 L400,140 L0,140 Z" fill="var(--red)"/>
      <path d="M0,140 Q140,40 400,22 L400,140 Z" fill="var(--paper)"/>
    </svg>

    <div class="other">
      <h2 class="section-title">Other <span class="hl-red">Services</span></h2>
      <div class="rule"></div>
      <ul class="tick-list">
        <li><svg viewBox="0 0 14 12"><path d="M1 6l4 4 8-9" stroke="var(--red)" stroke-width="2.4" fill="none"/></svg>Electronic tank location services</li>
        <li><svg viewBox="0 0 14 12"><path d="M1 6l4 4 8-9" stroke="var(--red)" stroke-width="2.4" fill="none"/></svg>Camera Snaking</li>
        <li><svg viewBox="0 0 14 12"><path d="M1 6l4 4 8-9" stroke="var(--red)" stroke-width="2.4" fill="none"/></svg>Emergency Septic Repairs</li>
        <li><svg viewBox="0 0 14 12"><path d="M1 6l4 4 8-9" stroke="var(--red)" stroke-width="2.4" fill="none"/></svg>Real Estate Septic Inspections</li>
      </ul>
    </div>

    <div class="care">
      <h2 class="section-title">Septic Maintenance <span class="hl-red">Recommendations</span></h2>
      <div class="rule"></div>
      <ul class="tick-list">
        <li><svg viewBox="0 0 14 12"><path d="M1 6l4 4 8-9" stroke="var(--red)" stroke-width="2.4" fill="none"/></svg>Keep coffee grounds from going down the drain</li>
        <li><svg viewBox="0 0 14 12"><path d="M1 6l4 4 8-9" stroke="var(--red)" stroke-width="2.4" fill="none"/></svg>Refrain from flushing down any petroleum based or feminine hygiene products</li>
        <li><svg viewBox="0 0 14 12"><path d="M1 6l4 4 8-9" stroke="var(--red)" stroke-width="2.4" fill="none"/></svg>Practice water conservation</li>
        <li><svg viewBox="0 0 14 12"><path d="M1 6l4 4 8-9" stroke="var(--red)" stroke-width="2.4" fill="none"/></svg>No diapers, grease, motor oil, paper towels, wipes, paint, or cigarettes should ever be flushed down the drains.</li>
        <li><svg viewBox="0 0 14 12"><path d="M1 6l4 4 8-9" stroke="var(--red)" stroke-width="2.4" fill="none"/></svg>Don’t use chemical maintenance packets, order our all natural septic packets to keep the all your bacteria happy! (ask your technician today)</li>
      </ul>
    </div>
    <div class="edge"></div>
  </section>

</main>
</body>
</html>
```